I dont have a logo yet. My mind in color is navy blue and khaki maybe a tiny bit of yellow but open to ideas. name of the business is Prairie Ridge Builders. Dedicated to all sorts of construction commerical and residential. Im Tomas Verdugo owner of business<br/>Address to business is 287 N. Marbury El Paso Tx 79925 <br/>Phone is 9156820374<br/>Id like round corners i also like the see thru card a little.<br/>Open to trademark quotes

Target Market(s)

Construction

Contact Information for Business Card

PRAIRIE RIDGE BUILDERS LLC

Tomas Verdugo
Director of Operations

Commercial & Residential

9156820374
PRAIRIE.R.BUILDERS@MAILHAVEN.NET

Colors
0355a3
fff3d1

Requirements
Must have
• ROUND CORNERS
• BLUE AND KHAKI AND CLEAR
• LOGO

```html
<!DOCTYPE html>
<html lang="en">
<head>
<meta charset="utf-8">
<title>Prairie Ridge Builders – Business Card</title>
<link href="https://fonts.googleapis.com/css2?family=Exo+2:wght@700&family=Arimo:wght@400;700&display=swap" rel="stylesheet">
<style>
  :root {
    --navy: #173a66;
    --navy-text: #1c3f73;
    --yellow: #fcc419;
    --white: #ffffff;
    --page: #e9e6df;
  }
  * { margin: 0; padding: 0; box-sizing: border-box; }
  html, body {
    width: 1189px; height: 1200px; overflow: hidden;
    background: var(--page);
    font-family: "Arimo", Arial, sans-serif;
  }
  .card {
    position: absolute;
    left: 169px;
    width: 852px;
    border-radius: 30px;
    overflow: hidden;
  }
  .card-front {
    top: 112px; height: 484px;
    background: var(--white);
    border-bottom: 8px solid var(--navy);
    color: var(--navy-text);
  }
  .card-back {
    top: 640px; height: 486px;
    background: var(--navy);
  }
  .accent-dot {
    position: absolute; left: -25px; top: 55px;
    width: 50px; height: 50px; border-radius: 50%;
    background: var(--yellow);
  }
  .holder { position: absolute; left: 46px; top: 56px; }
  .holder-name {
    font-family: "Exo 2", Arial, sans-serif;
    font-weight: 700; font-size: 25px; letter-spacing: 0.3px;
    line-height: 1.1;
  }
  .holder-title { font-size: 19px; margin-top: 2px; }
  .wordmark {
    position: absolute; right: 52px; top: 205px;
    font-weight: 700; font-size: 30px; line-height: 1.15;
    text-align: right; color: var(--navy-text);
  }
  .tagline {
    position: absolute; left: 46px; top: 311px;
    font-size: 19px; letter-spacing: 0.2px;
  }
  .rule {
    position: absolute; left: 46px; top: 344px;
    width: 755px; height: 3px; background: var(--yellow);
  }
  .contact {
    position: absolute; left: 46px; top: 399px;
    font-size: 19.5px; line-height: 27px;
  }
  .contact-row { display: flex; align-items: center; gap: 10px; }
  .contact-row svg { width: 16px; height: 16px; flex: none; }
  .address {
    position: absolute; right: 51px; top: 399px;
    font-size: 19.5px; line-height: 27px; text-align: right;
  }
  .wordmark-back {
    position: absolute; left: 0; right: 0; top: 205px;
    text-align: center; color: var(--white);
    font-weight: 700; font-size: 42px; line-height: 1.2;
  }
</style>
</head>
<body>
  <section class="card card-front">
    <div class="accent-dot"></div>
    <div class="holder">
      <div class="holder-name">TOMAS VERDUGO</div>
      <div class="holder-title">Director of Operations</div>
    </div>
    <div class="wordmark">PRAIRIE RIDGE<br>BUILDERS LLC</div>
    <div class="tagline">COMMERCIAL &amp; RESIDENTIAL</div>
    <div class="rule"></div>
    <div class="contact">
      <div class="contact-row">
        <svg viewBox="0 0 16 16" aria-hidden="true"><rect x="3.5" y="1" width="9" height="14" rx="1.5" fill="none" stroke="#fcc419" stroke-width="1.6"/><circle cx="8" cy="12.5" r="0.9" fill="#fcc419"/></svg>
        <span>915'682-0374</span>
      </div>
      <div class="contact-row">
        <svg viewBox="0 0 16 16" aria-hidden="true"><rect x="1" y="3" width="14" height="10" fill="#fcc419"/><path d="M1 3 L8 9 L15 3" fill="none" stroke="#ffffff" stroke-width="1.2"/></svg>
        <span>PRAIRIE.R.BUILDERS@MAILHAVEN.NET</span>
      </div>
    </div>
    <div class="address">287 N. MARBURY<br>EL PASO TX 79925</div>
  </section>

  <section class="card card-back">
    <div class="wordmark-back">PRAIRIE RIDGE<br>BUILDERS LLC</div>
  </section>
</body>
</html>
```